Business Card for Technology Startup

Design a 2-sided business card using the logo provided. We are a digital healthcare platform that provides a mobile app and web UI that helps caregivers, families, and doctors share information and provide better patient outcomes. We use AI and machine learning to help guide patients through their day-to-day life. The final design should communicate stability, peace, comfort, but also align with the image of an AI-driven technology startup.

I'd like the deliverable to by a Photoshop PSD file (with layers) that I can work with in pixlr.com. Should contain the following editable layers:
Name (ex. Karl Whitby)
Title (ex. Founder / CEO)
Email (ex. info@morventary.ai)
Phone (ex. (999) 482-7160)
Website (ex. https://morventary.ai)

```html
<!DOCTYPE html>
<html lang="en">
<head>
<meta charset="utf-8">
<title>Morventary Business Card</title>
<link rel="stylesheet" href="https://fonts.googleapis.com/css2?family=Poppins:wght@400;500;600;700&display=swap">
<style>
  :root {
    --backdrop: #999999;
    --card-white: #ffffff;
    --ink: #111111;
    --muted: #6b6b6b;
    --brand-blue: #0bbbe8;
    --brand-light: #72d0df;
    --brand-deep: #05b5e6;
  }
  * { margin: 0; padding: 0; box-sizing: border-box; }
  html, body {
    width: 1200px;
    height: 1000px;
    overflow: hidden;
    background: var(--backdrop);
    font-family: "Poppins", sans-serif;
  }
  .canvas {
    position: relative;
    width: 1200px;
    height: 1000px;
  }
  .card {
    position: absolute;
    left: 254px;
    width: 692px;
    height: 398px;
    border-radius: 24px;
    overflow: hidden;
  }
  .card--front {
    top: 70px;
    background: linear-gradient(90deg, var(--brand-deep) 0%, #3cbfe3 40%, var(--brand-light) 100%);
  }
  .card--back {
    top: 546px;
    background: var(--card-white);
  }
  .brand {
    position: absolute;
    left: 66px;
    top: 60px;
    display: flex;
    align-items: center;
    gap: 12px;
  }
  .brand__dot {
    width: 22px;
    height: 22px;
    border-radius: 50%;
    background: var(--brand-blue);
  }
  .brand__name {
    font-size: 36px;
    font-weight: 600;
    color: var(--ink);
    line-height: 1;
    letter-spacing: 0.2px;
  }
  .person__name {
    position: absolute;
    left: 66px;
    top: 164px;
    font-size: 23px;
    font-weight: 600;
    color: var(--brand-blue);
    text-transform: uppercase;
    line-height: 1;
  }
  .person__title {
    position: absolute;
    left: 65px;
    top: 192px;
    font-size: 14.5px;
    font-weight: 400;
    color: var(--ink);
    line-height: 1;
  }
  .contact {
    position: absolute;
    left: 66px;
    top: 238px;
    list-style: none;
  }
  .contact__item {
    display: flex;
    align-items: center;
    gap: 6px;
    height: 26px;
    font-size: 18px;
    color: var(--muted);
    line-height: 1;
  }
  .contact__icon {
    width: 15px;
    height: 15px;
    flex: none;
  }
  .website {
    position: absolute;
    left: 66px;
    top: 319px;
    font-size: 18.5px;
    line-height: 1;
    color: var(--muted);
  }
  .website__name {
    font-weight: 600;
    color: var(--brand-blue);
  }
  .decor {
    position: absolute;
    left: 332px;
    top: 0;
    width: 360px;
    height: 398px;
    background: linear-gradient(90deg, rgba(255,255,255,0) 0%, rgba(12,190,232,0.55) 25%, rgba(12,190,232,0.75) 45%, rgba(114,208,223,0.6) 80%, rgba(255,255,255,0) 100%);
  }
</style>
</head>
<body>
  <main class="canvas">
    <section class="card card--front" role="img" aria-label="Repeating pattern of the brand symbol on a blue gradient"></section>

    <section class="card card--back">
      <div class="brand">
        <span class="brand__dot"></span>
        <span class="brand__name">morventary</span>
      </div>

      <h1 class="person__name">Karl Whitby</h1>
      <p class="person__title">Founder / CEO</p>

      <ul class="contact">
        <li class="contact__item">
          <svg class="contact__icon" viewBox="0 0 16 16" fill="none" stroke="#0bbbe8" stroke-width="1.2" stroke-linejoin="round">
            <path d="M3 1.5l2.5 0 1 3.5-1.6 1.2a8 8 0 0 0 4.9 4.9L11 9.5l3.5 1 0 2.5a1.5 1.5 0 0 1-1.6 1.5C7 14 2 9 1.5 3.1A1.5 1.5 0 0 1 3 1.5z"/>
          </svg>
          <span>info@morventary.ai</span>
        </li>
        <li class="contact__item">
          <svg class="contact__icon" viewBox="0 0 16 16" fill="none" stroke="#0bbbe8" stroke-width="1.2" stroke-linejoin="round">
            <rect x="1" y="3.5" width="14" height="9"/>
            <path d="M1 3.5l7 5.5 7-5.5M1 12.5l5-4.5M15 12.5l-5-4.5"/>
          </svg>
          <span>(999) 482-7160</span>
        </li>
      </ul>

      <p class="website"><span class="website__name">morventary</span>.ai</p>

      <div class="decor" role="img" aria-label="Large decorative brand symbol in a blue gradient"></div>
    </section>
  </main>
</body>
</html>
```